Business Card Design Project (Beer industry)

I am seeking a redesign of my business card. I am looking for something that will really stand out in both texture and feel. Something more on the modern side then traditional. Nothing die cut shaped like a beer mug please.

The card is used mostly for other industry professionals, as well as bar and restaurant owners. My title is Strategy & Acquisitions. If you would like to somehow incorporate that theme, that may work.

My business is craft and imported beer. Nothing fizzy and yellow, so my products are more on the upscale side.
Updates

I was able to update my logo in .ai and .tif format. I hope that helps. 

Thank you all for your creative ideas. I have uploaded my current business card in pdf format, as well as our logo in .eps file format. We are excited about the submissions so far and want to thank you all again.

PS Please do not include fax number in future submissions, as we are looking for something more creative and a fax says 1999 and not 2015, which is the message we are going for, without being futuristic. 

Thank you all once again for all of your submissions. If we would consider a two sided card, we would like the opposite side not to be the same as the front. The styles we have seen so far, it appears the front and back are too similar. Again, a two sided card is not required. Thank you and we look forward to pushing the boundaries of your creativity. Cheers

Target Market(s)

My card would mostly go to bar and restaurant operators as well as other beer industry professionals

Industry/Entity Type

Restaurant

Requirements
Nice to have
• Two sided would be considered, although not required
Should not have
• Anything die cut shaped like a beer mug.

```html
<!DOCTYPE html>
<html lang="en">
<head>
<meta charset="utf-8">
<title>Kestrel Brew – Business Card</title>
<link rel="stylesheet" href="https://fonts.googleapis.com/css2?family=PT+Sans:wght@400;700&family=Cinzel:wght@400&display=swap">
<style>
  :root {
    --stage: #121212;
    --paper: #eceef0;
    --paper-edge: #d9dcdf;
    --band: #0b0b0b;
    --accent: #b3181c;
    --rule-grey: #9a9da1;
    --ink: #1a1a1a;
    --muted: #c9c9c9;
  }
  * { box-sizing: border-box; margin: 0; padding: 0; }
  html, body {
    width: 1200px; height: 901px; overflow: hidden;
    background: radial-gradient(ellipse at 50% 45%, #262626 0%, var(--stage) 70%);
    font-family: "PT Sans", Arial, sans-serif;
  }
  .card {
    position: absolute; left: 100px; top: 165px;
    width: 1000px; height: 571px;
    background: linear-gradient(160deg, #f7f8f9 0%, var(--paper) 55%, var(--paper-edge) 100%);
    overflow: hidden;
  }
  .band {
    position: absolute; left: 0; right: 0; top: 256px; height: 226px;
    background: var(--band);
    border-top: 6px solid var(--accent);
  }
  .band-rules {
    position: absolute; left: 0; right: 0; top: 482px;
    height: 12px;
    border-top: 5px solid var(--accent);
    border-bottom: 7px solid var(--rule-grey);
  }
  .brand {
    position: absolute; left: 70px; top: 176px;
    display: flex; align-items: center; gap: 12px;
    padding: 16px 22px;
    background: var(--paper);
  }
  .brand-mark { width: 22px; height: 22px; background: var(--accent); }
  .brand-name {
    font-weight: 700; font-size: 34px; letter-spacing: 2px;
    color: var(--accent);
  }
  .company {
    position: absolute; left: 70px; top: 300px;
    font-size: 22px; line-height: 28px; color: var(--muted);
  }
  .company .company-name { color: var(--accent); }
  .person {
    position: absolute; right: 70px; top: 168px; text-align: right;
  }
  .person-name { font-size: 38px; color: var(--ink); line-height: 1; }
  .person-title { font-size: 27px; color: var(--accent); margin-top: 4px; }
  .contact {
    position: absolute; right: 70px; top: 318px;
    list-style: none; color: #f2f2f2; font-size: 27px; line-height: 36px;
    text-align: left;
  }
  .contact li { display: flex; align-items: center; gap: 12px; }
  .contact .plain { padding-left: 0; }
  .contact svg { width: 18px; height: 22px; flex: none; }
  .tagline {
    position: absolute; left: 70px; top: 512px;
    font-family: "Cinzel", Georgia, serif; font-size: 25px; letter-spacing: 1.5px;
    color: var(--ink);
  }
</style>
</head>
<body>
  <main class="card">
    <div class="band"></div>
    <div class="band-rules"></div>

    <div class="brand">
      <span class="brand-mark"></span>
      <span class="brand-name">KESTREL BREW</span>
    </div>

    <address class="company" style="font-style:normal">
      <div class="company-name">Kestrel Brew Corp.</div>
      <div>42 Harlow Street</div>
      <div>Brooklyn, NY 11201</div>
    </address>

    <div class="person">
      <div class="person-name">Dan Corwell</div>
      <div class="person-title">Sales Manager</div>
    </div>

    <ul class="contact">
      <li>
        <svg viewBox="0 0 18 22" aria-hidden="true"><path d="M4 2c-2 1-3 3-2 6 2 5 5 9 9 12 2 1 4 0 5-1l-3-4-2 1c-2-1-4-4-5-6l2-1-2-5z" fill="var(--accent)"/></svg>
        (555) 301-4420
      </li>
      <li>
        <svg viewBox="0 0 18 22" aria-hidden="true"><rect x="3" y="2" width="12" height="18" rx="2" fill="none" stroke="var(--accent)" stroke-width="2.5"/></svg>
        (555) 302-7719
      </li>
      <li class="plain">dcorwell@mail.com</li>
      <li class="plain">www.kestrelbrew.com</li>
    </ul>

    <div class="tagline">Premiere Craft &amp; Import Beer Distributor</div>
  </main>
</body>
</html>
```